Create branded design templates/backgrounds for social media based on UK property investing company

I'd like Instagram, Facebook and Linkedin backgrounds/templates to add text to, based on my logo design and business of UK holiday let investing. Ideally I'd have some base designs for me to approve, then engage with the winning designer further to create about 50 different templates. I looking for a mixture of templates with the logo and using logo colours, others of internal holiday let photos including logos and a few of my photo imposed on the front of them.

Target Market(s)

Middle aged adults

Industry/Entity Type

Holiday let properties

Requirements
Must have
• a distinct brand look that can be replicated

```html
<!DOCTYPE html>
<html lang="en">
<head>
<meta charset="utf-8">
<title>Harbourline Homes – Social Post Set</title>
<link href="https://fonts.googleapis.com/css2?family=Anton&family=Comfortaa:wght@400;700&family=Great+Vibes&family=Marcellus&family=Montserrat:wght@400;500;700&display=swap" rel="stylesheet">
<style>
  :root{
    --bg:#353535;
    --white:#ffffff;
    --ink:#1c1c1c;
    --blue:#0a7fd0;
    --navy:#15407a;
    --green:#5aa80f;
    --green-deep:#4c9a0a;
    --yellow:#f2d21b;
  }
  *{margin:0;padding:0;box-sizing:border-box;}
  html,body{width:1200px;height:800px;overflow:hidden;background:var(--bg);}
  body{font-family:'Montserrat',sans-serif;position:relative;}
  .post-set{position:absolute;left:20px;top:210px;display:flex;gap:10px;}
  .post{position:relative;width:380px;height:380px;overflow:hidden;}

  .brand{display:flex;align-items:center;gap:5px;font-family:'Montserrat',sans-serif;font-weight:500;font-size:9px;letter-spacing:.3px;color:var(--navy);line-height:1;}
  .brand-square{width:10px;height:10px;background:var(--blue);}

  /* Post 1 */
  .post-intro .photo{position:absolute;inset:0;background:linear-gradient(180deg,#d9e5ec 0%,#a9c8dc 40%,#b9cbb2 62%,#6f9a3a 78%,#4f7f22 100%);}
  .post-intro .brand{position:absolute;left:18px;top:20px;}
  .intro-title{position:absolute;left:38px;top:84px;font-family:'Comfortaa',sans-serif;font-weight:400;font-size:22px;line-height:26px;color:#2a2a2a;}
  .intro-title strong{display:block;color:var(--blue);font-family:'Comfortaa',sans-serif;font-weight:700;font-size:22px;}
  .intro-rule{position:absolute;left:40px;top:188px;width:120px;height:2px;background:var(--green);}
  .post-intro .handle{position:absolute;left:31px;bottom:16px;font-size:9px;color:var(--white);letter-spacing:.3px;}

  /* Post 2 */
  .post-listing{background:var(--white);}
  .post-listing .handle{position:absolute;left:30px;top:14px;font-size:9px;color:var(--ink);}
  .post-listing .brand{position:absolute;right:28px;top:16px;}
  .listing-script{position:absolute;left:30px;top:44px;font-family:'Great Vibes',cursive;font-size:22px;color:var(--green);}
  .listing-photo{position:absolute;left:30px;top:74px;width:326px;height:217px;background:linear-gradient(180deg,#c9d9e6 0%,#e6ecef 45%,#cfd3cf 70%,#4f8a2a 100%);}
  .family-photo{position:absolute;left:222px;top:150px;width:158px;height:230px;background:linear-gradient(180deg,#ddd8d3 0%,#f1f1f1 55%,#e9e9e9 100%);border-top-left-radius:60px;border-top-right-radius:30px;}
  .listing-title{position:absolute;left:40px;top:88px;font-family:'Marcellus',serif;font-size:22px;line-height:29px;color:var(--blue);}
  .budget-label{position:absolute;left:36px;top:296px;font-size:10px;letter-spacing:2px;color:var(--ink);}
  .budget-value{position:absolute;left:36px;top:308px;font-family:'Marcellus',serif;font-size:25px;color:var(--green);}
  .budget-value span{font-family:'Montserrat',sans-serif;font-size:9px;color:var(--ink);}
  .address{position:absolute;left:18px;top:338px;display:flex;align-items:center;gap:8px;}
  .address p{font-size:7px;font-weight:700;letter-spacing:1px;color:#333;line-height:10px;}
  .address-rule{position:absolute;left:40px;top:364px;width:160px;height:1px;background:#bbb;}

  /* Post 3 */
  .post-cta{background:linear-gradient(180deg,var(--green) 0%,var(--green-deep) 100%);}
  .cta-photo{position:absolute;left:0;top:0;width:380px;height:200px;background:linear-gradient(180deg,#a7c78a 0%,#8db865 60%,rgba(90,168,15,0) 100%);}
  .cta-tab{position:absolute;left:-20px;top:-20px;width:100px;height:80px;background:var(--white);border-bottom-right-radius:22px;transform:skewX(-18deg);}
  .post-cta .brand{position:absolute;left:10px;top:18px;font-size:6px;}
  .post-cta .brand-square{width:8px;height:8px;}
  .cta-title{position:absolute;left:0;width:380px;top:146px;text-align:center;font-family:'Anton',sans-serif;font-weight:400;font-size:43px;line-height:46px;color:var(--white);letter-spacing:.5px;}
  .cta-script{position:absolute;left:206px;top:236px;font-family:'Great Vibes',cursive;font-size:28px;line-height:30px;color:var(--yellow);}
  .cta-rule{position:absolute;left:62px;top:251px;width:130px;height:2px;background:var(--yellow);}
  .cta-copy{position:absolute;left:60px;width:260px;top:279px;text-align:center;font-size:8px;line-height:12px;color:var(--white);}
  .cta-pill{position:absolute;left:58px;top:315px;width:263px;height:33px;background:var(--white);border-radius:6px;display:flex;align-items:center;padding:0 14px;gap:6px;white-space:nowrap;}
  .cta-pill svg{flex:none;}
  .cta-pill .label{font-family:'Anton',sans-serif;font-size:14px;line-height:1;color:var(--blue);letter-spacing:.3px;white-space:nowrap;flex:none;}
  .cta-pill .dots{flex:none;width:3px;height:14px;margin:0 10px;background:radial-gradient(circle,var(--green) 1.3px,transparent 1.5px) 0 0/3px 5px;}
  .cta-pill .site{font-size:8px;color:var(--ink);white-space:nowrap;}
  .cta-corner{position:absolute;right:-14px;bottom:-14px;width:40px;height:60px;background:var(--blue);border-radius:20px 0 0 0;border-left:4px solid var(--yellow);}
</style>
</head>
<body>
<main class="post-set">

  <section class="post post-intro">
    <div class="photo" role="img" aria-label="Photo of a woman lying in a meadow holding a wooden house frame up to the sky"></div>
    <div class="brand"><span class="brand-square"></span>Harbourline Homes</div>
    <h1 class="intro-title">Holiday<br>Home a<strong>Good<br>Investment</strong></h1>
    <div class="intro-rule"></div>
    <p class="handle">@harbourlinehomes</p>
  </section>

  <section class="post post-listing">
    <p class="handle">@harbourlinehomes</p>
    <div class="brand"><span class="brand-square"></span>Harbourline Homes</div>
    <p class="listing-script">Perfect Luxury</p>
    <div class="listing-photo" role="img" aria-label="Photo of a modern white holiday villa with a green lawn"></div>
    <div class="family-photo" role="img" aria-label="Photo of a smiling family with a child on the father's shoulders"></div>
    <h2 class="listing-title">HOLIDAY HOME<br>A GOOD<br>INVESTMENT</h2>
    <p class="budget-label">BUDGET:</p>
    <p class="budget-value">6.75CR <span>Onwards</span></p>
    <div class="address">
      <svg width="28" height="28" viewBox="0 0 28 28" aria-hidden="true"><circle cx="14" cy="14" r="14" fill="#0a7fd0"/><path d="M14 6a5 5 0 0 0-5 5c0 4 5 10 5 10s5-6 5-10a5 5 0 0 0-5-5z" fill="#fff"/><circle cx="14" cy="11" r="2" fill="#0a7fd0"/></svg>
      <p>48 QUAY LANE, SEAFORD,<br>BN25 1AA</p>
    </div>
    <div class="address-rule"></div>
  </section>

  <section class="post post-cta">
    <div class="cta-photo" role="img" aria-label="Photo of a scale model house on architectural blueprints"></div>
    <div class="cta-tab"></div>
    <div class="brand"><span class="brand-square"></span>Harbourline Homes</div>
    <h2 class="cta-title">THE SMARTEST<br>WAY TO INVEST</h2>
    <div class="cta-rule"></div>
    <p class="cta-script">With Us</p>
    <p class="cta-copy">Build your dream house with us! Our expert team will guide you every step of the way. Contact us now!</p>
    <div class="cta-pill">
      <svg width="16" height="16" viewBox="0 0 16 16" aria-hidden="true"><circle cx="8" cy="8" r="8" fill="#0a7fd0"/><rect x="4" y="5" width="8" height="6" rx="1" fill="#fff"/><path d="M4.3 5.4L8 8.3l3.7-2.9" stroke="#0a7fd0" stroke-width="1" fill="none"/></svg>
      <span class="label">CONTACT US</span>
      <span class="dots"></span>
      <span class="site">www.harbourlinehomes.com</span>
    </div>
    <div class="cta-corner"></div>
  </section>

</main>
</body>
</html>
```